KFR T Coaching Website

We need a website to post videos, blogs and other information or links.
We teach Jujitsu , combatives, Metaphysical Coaching. I want to tach online and in person. Silver Harbor Institute Deals in several areas of Personal Protection and Coaching.
Training (Martial Arts / combative)
Emotional Intelligence
Leadership Development
Motivation
Our Log is attached.
Similar Websites to what we do ( we want to stand out better).
https://renwoskel.com/
https://bavomure.com/
https://crestlinevigorcoaching.com/
Training , Martial Arts, coaching
2 page

```html
<!DOCTYPE html>
<html lang="en">
<head>
<meta charset="utf-8">
<title>Silver Harbor Institute — Martial Arts Training Platform</title>
<link href="https://fonts.googleapis.com/css2?family=Poppins:wght@400;500;600;700&family=Inter:wght@400;500;600&display=swap" rel="stylesheet">
<style>
:root{
  --ink:#1a1a1a;
  --muted:#6b6b6b;
  --line:#dedede;
  --purple:#5a2d82;
  --orange:#e2781d;
  --peach:#fcd6ae;
  --green:#3b9b4d;
  --dark:#141414;
  --white:#ffffff;
  --soft:#f4f4f4;
}
*{box-sizing:border-box;margin:0;padding:0}
html,body{width:1200px;height:5300px;overflow:hidden}
body{background:var(--white);color:var(--ink);font-family:"Inter",Arial,sans-serif;font-size:13px;position:relative}
h1,h2,h3,h4{font-family:"Poppins",Arial,sans-serif}
.wrap{position:absolute;left:60px;width:1080px}

/* header */
.site-header{position:absolute;top:0;left:0;width:1200px;height:70px;display:flex;align-items:center;padding:0 60px;justify-content:space-between}
.brand{display:flex;align-items:center;gap:8px;font-family:"Poppins",sans-serif;font-weight:600;font-size:13px}
.brand-dot{width:22px;height:22px;border-radius:50%;background:var(--ink)}
.main-nav{display:flex;gap:22px;font-size:13px;font-weight:500}
.social{display:flex;gap:10px}
.social span{width:14px;height:14px;border-radius:50%;background:var(--ink);display:block}

/* hero */
.hero{top:100px;height:430px;background:linear-gradient(90deg,#6e6e6e 0%,#a9a9a9 45%,#e9e9e9 100%);overflow:hidden}
.hero-photo{position:absolute;right:0;top:0;width:560px;height:430px;background:linear-gradient(160deg,#f3f3f3,#d9d9d9)}
.hero-text{position:absolute;left:36px;top:250px;width:500px;color:var(--white)}
.hero-text h1{font-size:27px;font-weight:600;margin-bottom:10px}
.hero-text p{font-size:12px;line-height:1.55}
.dots{position:absolute;bottom:14px;left:50%;display:flex;gap:7px;transform:translateX(-50%)}
.dots i{width:7px;height:7px;border-radius:50%;background:rgba(255,255,255,.6)}
.dots i:first-child{background:var(--white)}

/* promo */
.promo{top:600px;height:272px;background:var(--peach);padding:44px 0 0 130px}
.promo .kicker{color:var(--purple);font-size:13px;font-weight:500}
.promo h2{font-size:29px;line-height:1.22;font-weight:600;color:var(--ink);width:690px;white-space:nowrap}
.promo h2 .hl{color:var(--orange)}
.promo .deadline{margin-top:6px;font-size:13px;font-weight:600}
.promo .deadline b{color:var(--orange)}
.btn-green{display:inline-block;margin-top:14px;background:var(--green);color:var(--white);font-size:11px;font-weight:600;letter-spacing:1px;padding:9px 20px;border-radius:3px}
.promo-art{position:absolute;right:50px;top:36px;width:180px;height:200px;border-radius:10px;background:linear-gradient(160deg,#f7c48f,#f0a866)}

/* headings */
.sec-title{font-size:24px;font-weight:600}
.center{text-align:center}
.sub{font-size:12px;color:var(--ink);margin-top:10px}

/* course cards */
.cards{display:grid;grid-template-columns:repeat(4,1fr);gap:28px}
.course-img{height:175px}
.course h3{font-size:15px;font-weight:600;margin:12px 0 8px}
.course p{font-size:11px;line-height:1.55;color:var(--muted)}
.course-actions{display:flex;justify-content:space-between;align-items:center;margin-top:14px}
.btn-purple{background:var(--purple);color:var(--white);font-size:11px;font-weight:600;padding:9px 20px;border-radius:3px}
.fav{width:30px;height:30px;border:1px solid #999;border-radius:50%;display:flex;align-items:center;justify-content:center}

/* scholarship */
.scholar{top:1512px;height:268px;border-radius:6px;box-shadow:0 2px 14px rgba(0,0,0,.12);padding:40px 50px}
.scholar h2{font-size:36px;font-weight:500}
.scholar .lead{font-size:14px;font-weight:600;margin-top:6px}
.perks{display:flex;gap:18px;margin-top:10px;font-size:11px;color:var(--muted)}
.perks span::before{content:"";display:inline-block;width:7px;height:7px;border-radius:50%;background:var(--ink);margin-right:6px}
.btn-dark{display:inline-block;margin-top:16px;background:#2a2a2a;color:var(--white);font-size:11px;font-weight:600;padding:10px 20px;border-radius:3px}
.scholar-art{position:absolute;right:200px;top:40px;width:170px;height:170px;border-radius:50%;background:linear-gradient(160deg,#ffe09a,#7fb3e6)}

/* popular */
.pop-card{border:1px solid #cfcfcf;height:168px;padding:16px 16px}
.pop-card .cat{font-size:11px;padding-bottom:10px;border-bottom:1px solid var(--line)}
.pop-card h4{font-size:17px;font-weight:500;line-height:1.3;margin-top:12px}
.pop-card .by{font-size:11px;color:var(--muted);margin-top:24px}

/* article lists */
.art-head{display:flex;justify-content:space-between;align-items:center}
.art-head h2{font-size:20px;font-weight:600}
.btn-view{background:#111;color:var(--white);font-size:10px;font-weight:600;letter-spacing:.5px;padding:9px 18px;border-radius:3px}
.art-grid{display:grid;grid-template-columns:repeat(4,1fr);margin-top:30px}
.art{padding:0 16px;border-left:1px solid var(--line)}
.art:first-child{border-left:none;padding-left:0}
.art h3{font-size:14px;font-weight:600;line-height:1.35}
.art p{font-size:11.5px;line-height:1.5;margin-top:8px;color:#333}
.meta{display:flex;justify-content:space-between;font-size:9.5px;color:var(--muted);margin-top:12px}
.author{display:flex;align-items:center;gap:10px;font-size:10px;margin-top:14px}
.author i{width:22px;height:22px;border-radius:50%;background:#333;display:block}
.rule{position:absolute;left:60px;width:1080px;border-top:1px solid #999}

/* contact */
.contact-info{display:grid;grid-template-columns:repeat(3,1fr);text-align:center}
.contact-info div{border-left:1px solid var(--line);padding:6px 0}
.contact-info div:first-child{border-left:none}
.contact-info h4{font-size:12px;letter-spacing:1px;font-weight:600;margin:14px 0 8px}
.contact-info p{font-size:11px;color:#333}
.form{top:4455px;height:290px;background:var(--soft);padding:18px 36px}
.form .row{display:flex;gap:14px}
.field{background:var(--white);border:1px solid var(--line);height:34px;font-size:11px;color:#777;padding:10px 12px;flex:1;margin-bottom:12px}
.field.tall{height:110px}
.send{display:block;width:160px;margin:6px auto 0;background:#111;color:var(--white);text-align:center;font-size:11px;padding:11px 0;border-radius:3px}

/* footer */
.site-footer{position:absolute;top:4790px;left:0;width:1200px;height:510px;background:var(--dark);color:#d8d8d8}
.foot-cols{position:absolute;left:60px;top:40px;width:1080px;display:grid;grid-template-columns:270px 190px 260px 360px}
.foot-cols h4{color:var(--white);font-size:14px;font-weight:600;margin-bottom:16px}
.foot-brand{color:var(--white);font-family:"Poppins",sans-serif;font-weight:600;font-size:18px;margin-bottom:14px}
.foot-cols p{font-size:11px;line-height:1.6;padding-right:20px}
.foot-social{display:flex;gap:10px;margin-top:16px}
.foot-social span{width:16px;height:16px;border-radius:50%;background:var(--white);display:block}
.links li{list-style:none;font-size:11px;margin-bottom:10px}
.links li::before{content:"› ";color:#999}
.post{display:flex;gap:10px;margin-bottom:12px;font-size:11px;line-height:1.4}
.post i{width:44px;height:32px;background:linear-gradient(135deg,#555,#888);flex:none;display:block}
.post small{display:block;color:#999;font-size:9px}
.copy{position:absolute;left:60px;bottom:36px;font-size:11px;border-top:1px solid #333;width:1080px;padding-top:14px}
</style>
</head>
<body>

<header class="site-header">
  <div class="brand"><span class="brand-dot"></span>Silver Harbor Institute</div>
  <nav class="main-nav"><span>Home</span><span>Blog</span><span>About Us</span><span>Categories ▾</span><span>Service</span><span>Contact Us</span><span>Log In</span></nav>
  <div class="social"><span></span><span></span><span></span><span></span></div>
</header>

<section class="wrap hero">
  <div class="hero-photo" role="img" aria-label="Martial artist in white uniform performing a flying kick"></div>
  <div class="hero-text">
    <h1>Best Martial Arts Training Platform</h1>
    <p>Lorem ipsum dolor sit amet, consectetur adipiscing elit. Quidem neque est muchis! Beatae minima accusantium repellat harum rem, omnis quam magnam voluptatem aut dolore ipsam quibusdam commodi facere hic corporis explicabo consectetur sit ab.</p>
  </div>
  <div class="dots"><i></i><i></i><i></i></div>
</section>

<section class="wrap promo">
  <div class="kicker">Online Courses</div>
  <h2>Are You Ready For This Amazing Session<br>Get Up to <span class="hl">20% Off</span> on All Subscriptions</h2>
  <div class="deadline">Offer End <b>22 September 6:30 PM</b></div>
  <span class="btn-green">SUBSCRIBE NOW</span>
  <div class="promo-art" role="img" aria-label="Illustration of a trophy and gift boxes"></div>
</section>

<h2 class="wrap sec-title" style="top:905px">Expand your career opportunities with Silver Harbor</h2>

<section class="wrap cards" style="top:995px">
  <article class="course"><div class="course-img" role="img" aria-label="Person climbing a stepped word sculpture" style="background:linear-gradient(160deg,#d9a85c,#3a3024)"></div><h3>Motivational Training</h3><p>Lorem ipsum dolor sit amet consectetur adipiscing elit. Saepe debitis quibusdam assumenda nemo, cum eos.</p><div class="course-actions"><span class="btn-purple">Get Start</span><span class="fav"><svg width="14" height="13" viewBox="0 0 24 22"><path d="M12 20s-9-5.6-9-12a5 5 0 0 1 9-3 5 5 0 0 1 9 3c0 6.4-9 12-9 12z" fill="none" stroke="#555" stroke-width="2"/></svg></span></div></article>
  <article class="course"><div class="course-img" role="img" aria-label="Glowing blue brain concept artwork" style="background:linear-gradient(160deg,#2b7bd6,#7cc4f0)"></div><h3>Emotional Intelligence</h3><p>Lorem ipsum dolor sit amet consectetur adipiscing elit. Saepe debitis quibusdam assumenda nemo, cum eos.</p><div class="course-actions"><span class="btn-purple">Get Start</span><span class="fav"><svg width="14" height="13" viewBox="0 0 24 22"><path d="M12 20s-9-5.6-9-12a5 5 0 0 1 9-3 5 5 0 0 1 9 3c0 6.4-9 12-9 12z" fill="none" stroke="#555" stroke-width="2"/></svg></span></div></article>
  <article class="course"><div class="course-img" role="img" aria-label="Two martial artists sparring on a mat" style="background:linear-gradient(160deg,#5a8fd0,#c9d4e2)"></div><h3>Martial Arts Training</h3><p>Lorem ipsum dolor sit amet consectetur adipiscing elit. Saepe debitis quibusdam assumenda nemo, cum eos.</p><div class="course-actions"><span class="btn-purple">Get Start</span><span class="fav"><svg width="14" height="13" viewBox="0 0 24 22"><path d="M12 20s-9-5.6-9-12a5 5 0 0 1 9-3 5 5 0 0 1 9 3c0 6.4-9 12-9 12z" fill="none" stroke="#555" stroke-width="2"/></svg></span></div></article>
  <article class="course"><div class="course-img" role="img" aria-label="Team leadership concept photo" style="background:linear-gradient(160deg,#e6e2dc,#8c97a8)"></div><h3>Leadership Development</h3><p>Lorem ipsum dolor sit amet consectetur adipiscing elit. Saepe debitis quibusdam assumenda nemo, cum eos.</p><div class="course-actions"><span class="btn-purple">Get Start</span><span class="fav"><svg width="14" height="13" viewBox="0 0 24 22"><path d="M12 20s-9-5.6-9-12a5 5 0 0 1 9-3 5 5 0 0 1 9 3c0 6.4-9 12-9 12z" fill="none" stroke="#555" stroke-width="2"/></svg></span></div></article>
</section>

<div class="wrap center" style="top:1405px"><h2 class="sec-title">Traiding Now</h2><p class="sub">Lorem ipsum dolor sit amet consectetur adipiscing elit. Nesciunt excepturi quo ut debitis aperiam doloremque natus neque necessitatibus dolores accusantium!</p></div>

<section class="wrap scholar">
  <h2>Win scholarship upto 50%</h2>
  <p class="lead">The scholarship applies directly to your subscription</p>
  <div class="perks"><span>Get 50% subscription price to be won</span><span>15 quick questions</span><span>Just 15 min</span></div>
  <span class="btn-dark">START TEST</span>
  <div class="scholar-art" role="img" aria-label="Illustration of a graduation cap on a stack of books"></div>
</section>

<section class="wrap cards" style="top:1805px">
  <article class="course"><div class="course-img" role="img" aria-label="Jujitsu athlete in a dark dojo" style="background:linear-gradient(160deg,#1c1c1c,#6b6b6b)"></div><h3>Jujitsu Training</h3><p>Lorem ipsum dolor sit amet consectetur adipiscing elit. Saepe debitis quibusdam assumenda nemo, cum eos voluptas doloribus.</p><div class="course-actions"><span class="btn-purple">Add To Cart</span><span class="fav"><svg width="14" height="13" viewBox="0 0 24 22"><path d="M12 20s-9-5.6-9-12a5 5 0 0 1 9-3 5 5 0 0 1 9 3c0 6.4-9 12-9 12z" fill="none" stroke="#555" stroke-width="2"/></svg></span></div></article>
  <article class="course"><div class="course-img" role="img" aria-label="Thoughtful person portrait" style="background:linear-gradient(160deg,#8a6a4a,#2e241c)"></div><h3>Emotional Intelligence</h3><p>Lorem ipsum dolor sit amet consectetur adipiscing elit. Saepe debitis quibusdam assumenda nemo, cum eos voluptas doloribus.</p><div class="course-actions"><span class="btn-purple">Add To Cart</span><span class="fav"><svg width="14" height="13" viewBox="0 0 24 22"><path d="M12 20s-9-5.6-9-12a5 5 0 0 1 9-3 5 5 0 0 1 9 3c0 6.4-9 12-9 12z" fill="none" stroke="#555" stroke-width="2"/></svg></span></div></article>
  <article class="course"><div class="course-img" role="img" aria-label="Coach guiding students in a training hall" style="background:linear-gradient(160deg,#d8d3cc,#8c8277)"></div><h3>Metaphysical Coaching</h3><p>Lorem ipsum dolor sit amet consectetur adipiscing elit. Saepe debitis quibusdam assumenda nemo, cum eos voluptas doloribus.</p><div class="course-actions"><span class="btn-purple">Add To Cart</span><span class="fav"><svg width="14" height="13" viewBox="0 0 24 22"><path d="M12 20s-9-5.6-9-12a5 5 0 0 1 9-3 5 5 0 0 1 9 3c0 6.4-9 12-9 12z" fill="none" stroke="#555" stroke-width="2"/></svg></span></div></article>
  <article class="course"><div class="course-img" role="img" aria-label="Leader concept with chalkboard" style="background:linear-gradient(160deg,#3d5a80,#c3cfdc)"></div><h3>Leadership Development</h3><p>Lorem ipsum dolor sit amet consectetur adipiscing elit. Saepe debitis quibusdam assumenda nemo, cum eos voluptas doloribus.</p><div class="course-actions"><span class="btn-purple">Add To Cart</span><span class="fav"><svg width="14" height="13" viewBox="0 0 24 22"><path d="M12 20s-9-5.6-9-12a5 5 0 0 1 9-3 5 5 0 0 1 9 3c0 6.4-9 12-9 12z" fill="none" stroke="#555" stroke-width="2"/></svg></span></div></article>
</section>

<h2 class="wrap sec-title center" style="top:2232px">Populer Articles</h2>
<section class="wrap cards" style="top:2312px;gap:22px">
  <article class="pop-card"><div class="cat">Motivational Training</div><h4>How to Develop Your Mind Strength</h4><div class="by">Silver Harbor</div></article>
  <article class="pop-card"><div class="cat">Emotional Intelligence</div><h4>How to Develop Your Mind Strength</h4><div class="by">Silver Harbor</div></article>
  <article class="pop-card"><div class="cat">Martial Arts Training</div><h4>How to Develop Your Body Strength</h4><div class="by">Silver Harbor</div></article>
  <article class="pop-card"><div class="cat">Leadership Development</div><h4>How to Develop Your Business Knowledge</h4><div class="by">Silver Harbor</div></article>
</section>

<section class="wrap" style="top:2572px">
  <div class="art-head"><h2>Martial Arts Articles</h2><span class="btn-view">VIEW ALL POST</span></div>
  <div class="art-grid">
    <article class="art"><h3>Top Motivational Speech for Your Career</h3><p>Lorem ipsum dolor sit amet consectetur, adipiscing elit. Saepe debitis quibusdam assumenda nemo, cum eos.</p><div class="meta"><span>Update</span><span>Rem : 24-4-10</span></div><div class="author"><i></i>Silver Harbor</div></article>
    <article class="art"><h3>Top Motivational Speech for Your Career</h3><p>Lorem ipsum dolor sit amet consectetur, adipiscing elit. Saepe debitis quibusdam assumenda nemo, cum eos.</p><div class="meta"><span>Update</span><span>Rem : 24-4-10</span></div><div class="author"><i></i>Silver Harbor</div></article>
    <article class="art"><h3>Top Motivational Speech for Your Career</h3><p>Lorem ipsum dolor sit amet consectetur, adipiscing elit. Saepe debitis quibusdam assumenda nemo, cum eos.</p><div class="meta"><span>Update</span><span>Rem : 24-4-10</span></div><div class="author"><i></i>Silver Harbor</div></article>
    <article class="art"><h3>Top Motivational Speech for Your Career</h3><p>Lorem ipsum dolor sit amet consectetur, adipiscing elit. Saepe debitis quibusdam assumenda nemo, cum eos.</p><div class="meta"><span>Update</span><span>Rem : 24-4-10</span></div><div class="author"><i></i>Silver Harbor</div></article>
  </div>
</section>
<div class="rule" style="top:2908px"></div>

<section class="wrap" style="top:2960px">
  <div class="art-head"><h2>Motivational Articles</h2><span class="btn-view">VIEW ALL POST</span></div>
  <div class="art-grid">
    <article class="art"><h3>Top Martial Arts and Combative for Body Strength</h3><p>Lorem ipsum dolor sit amet consectetur, adipiscing elit. Saepe debitis quibusdam assumenda nemo, cum eos.</p><div class="meta"><span>Update</span><span>Rem : 24-4-10</span></div><div class="author"><i></i>Silver Harbor</div></article>
    <article class="art"><h3>Top Martial Arts and Combative for Body Strength</h3><p>Lorem ipsum dolor sit amet consectetur, adipiscing elit. Saepe debitis quibusdam assumenda nemo, cum eos.</p><div class="meta"><span>Update</span><span>Rem : 24-4-10</span></div><div class="author"><i></i>Silver Harbor</div></article>
    <article class="art"><h3>Top Martial Arts and Combative for Body Strength</h3><p>Lorem ipsum dolor sit amet consectetur, adipiscing elit. Saepe debitis quibusdam assumenda nemo, cum eos.</p><div class="meta"><span>Update</span><span>Rem : 24-4-10</span></div><div class="author"><i></i>Silver Harbor</div></article>
    <article class="art"><h3>Top Martial Arts and Combative for Your Body Strength</h3><p>Lorem ipsum dolor sit amet consectetur, adipiscing elit. Saepe debitis quibusdam assumenda nemo, cum eos.</p><div class="meta"><span>Update</span><span>Rem : 24-4-10</span></div><div class="author"><i></i>Silver Harbor</div></article>
  </div>
</section>
<div class="rule" style="top:3312px"></div>

<section class="wrap" style="top:3390px">
  <div class="art-head"><h2>Emotional Intelligence Articles</h2><span class="btn-view">VIEW ALL POST</span></div>
  <div class="art-grid">
    <article class="art"><h3>Top Emotional Intelligence Course for Your Career</h3><p>Lorem ipsum dolor sit amet consectetur, adipiscing elit. Saepe debitis quibusdam assumenda nemo, cum eos.</p><div class="meta"><span>Update</span><span>Rem : 24-4-10</span></div><div class="author"><i></i>Silver Harbor</div></article>
    <article class="art"><h3>Top Emotional Intelligence Course for Your Career</h3><p>Lorem ipsum dolor sit amet consectetur, adipiscing elit. Saepe debitis quibusdam assumenda nemo, cum eos.</p><div class="meta"><span>Update</span><span>Rem : 24-4-10</span></div><div class="author"><i></i>Silver Harbor</div></article>
    <article class="art"><h3>Top Emotional Intelligence Course for Your Career</h3><p>Lorem ipsum dolor sit amet consectetur, adipiscing elit. Saepe debitis quibusdam assumenda nemo, cum eos.</p><div class="meta"><span>Update</span><span>Rem : 24-4-10</span></div><div class="author"><i></i>Silver Harbor</div></article>
    <article class="art"><h3>Top Emotional Intelligence Course for Your Career</h3><p>Lorem ipsum dolor sit amet consectetur, adipiscing elit. Saepe debitis quibusdam assumenda nemo, cum eos.</p><div class="meta"><span>Update</span><span>Rem : 24-4-10</span></div><div class="author"><i></i>Silver Harbor</div></article>
  </div>
</section>
<div class="rule" style="top:3740px"></div>

<section class="wrap" style="top:3812px">
  <div class="art-head"><h2>Leadership Development Articles</h2><span class="btn-view">VIEW ALL POST</span></div>
  <div class="art-grid">
    <article class="art"><h3>Top Leadership Development Course For Your Career</h3><p>Lorem ipsum dolor sit amet consectetur, adipiscing elit. Saepe debitis quibusdam assumenda nemo, cum eos.</p><div class="meta"><span>Update</span><span>Rem : 24-4-10</span></div><div class="author"><i></i>Silver Harbor</div></article>
    <article class="art"><h3>Top Leadership Development Course For Your Career</h3><p>Lorem ipsum dolor sit amet consectetur, adipiscing elit. Saepe debitis quibusdam assumenda nemo, cum eos.</p><div class="meta"><span>Update</span><span>Rem : 24-4-10</span></div><div class="author"><i></i>Silver Harbor</div></article>
    <article class="art"><h3>Top Leadership Development Course For Your Career</h3><p>Lorem ipsum dolor sit amet consectetur, adipiscing elit. Saepe debitis quibusdam assumenda nemo, cum eos.</p><div class="meta"><span>Update</span><span>Rem : 24-4-10</span></div><div class="author"><i></i>Silver Harbor</div></article>
    <article class="art"><h3>Top Leadership Development Course For Your Career</h3><p>Lorem ipsum dolor sit amet consectetur, adipiscing elit. Saepe debitis quibusdam assumenda nemo, cum eos.</p><div class="meta"><span>Update</span><span>Rem : 24-4-10</span></div><div class="author"><i></i>Silver Harbor</div></article>
  </div>
</section>

<h2 class="wrap sec-title center" style="top:4200px;font-size:32px">Contact us</h2>
<section class="wrap contact-info" style="top:4280px">
  <div><svg width="24" height="30" viewBox="0 0 24 30"><path d="M12 28S3 17 3 11a9 9 0 0 1 18 0c0 6-9 17-9 17z" fill="none" stroke="#111" stroke-width="2"/><circle cx="12" cy="11" r="3.5" fill="none" stroke="#111" stroke-width="2"/></svg><h4>ADDRESS</h4><p>3108 Cedar Lane, WA 50025, USA</p></div>
  <div><svg width="22" height="30" viewBox="0 0 22 30"><rect x="3" y="2" width="16" height="26" rx="3" fill="none" stroke="#111" stroke-width="2"/><line x1="9" y1="24" x2="13" y2="24" stroke="#111" stroke-width="2"/></svg><h4>PHONE NUMBER</h4><p>+1 555 014 2278</p></div>
  <div><svg width="30" height="30" viewBox="0 0 30 30"><rect x="3" y="7" width="24" height="17" rx="2" fill="none" stroke="#111" stroke-width="2"/><path d="M3 8l12 9 12-9" fill="none" stroke="#111" stroke-width="2"/></svg><h4>EMAIL</h4><p>hello@silverharbor.example</p></div>
</section>

<section class="wrap form">
  <div class="row"><div class="field">Your Name</div><div class="field">Your Email</div></div>
  <div class="row"><div class="field">Subject</div></div>
  <div class="row"><div class="field tall">Message</div></div>
  <span class="send">Send Message</span>
</section>

<footer class="site-footer">
  <div class="foot-cols">
    <div>
      <div class="foot-brand">Silver Harbor Institute</div>
      <p>Lorem ipsum dolor sit amet consectetur adipiscing elit. Magnam ab, perspiciatis laudantium delectus voluptate nulla a dolores, commodi quibusdam illo dolorem laudantium recusandae officiis aut aliquid.</p>
      <div class="foot-social"><span></span><span></span><span></span><span></span><span></span></div>
    </div>
    <div><h4>Quick Links</h4><ul class="links"><li>Home</li><li>Blog</li><li>About Us</li><li>Categories</li><li>Service us</li><li>Contact</li></ul></div>
    <div><h4>Categories</h4><ul class="links"><li>Emotional Intelligence</li><li>Motivation</li><li>Leadership Development</li><li>Martial Arts</li><li>Combative</li><li>Metaphysical</li><li>Coaching</li></ul></div>
    <div><h4>Recent Posts</h4>
      <div class="post"><i role="img" aria-label="Post thumbnail"></i><div>We are Just Checking for Martial Arts / Combative Session You Can Join Now<small>Sep 12, 2023</small></div></div>
      <div class="post"><i role="img" aria-label="Post thumbnail"></i><div>See Our Motivational Videos And Motivate Yourself<small>Sep 10, 2023</small></div></div>
      <div class="post"><i role="img" aria-label="Post thumbnail"></i><div>Watch Our Emotional Intelligence Videos And Boost Yourself<small>Sep 08, 2023</small></div></div>
      <div class="post"><i role="img" aria-label="Post thumbnail"></i><div>6 Great Startup Tips for Female Founders<small>Sep 05, 2023</small></div></div>
    </div>
  </div>
  <div class="copy">Copyright By All Rights Reserved</div>
</footer>

</body>
</html>
```